Construction Business Card Design

We have a landscape construction company based in Australia
Were out of business cards ,
So now we're after a fresh looking modern card to give a fresh look to our business ....
We would like the business card to have the
(Front)
Tallow Ridge Pty Ltd
Director Norman Cusk
0462395108
(Back)
Landscape,Construction,Paving,Excavation
(In smaller font low in the frame of card)
Different textures , curved edge , vertical and horizontal designs also minimal colours per design
Eg one side black , one coloured or a splash here or there
Industry/Entity Type
Landscape
Contact Information for Business Card
Tallow Ridge Pty Ltd
Director Norman Cusk
0462395108
Landscape,Paving,Construction,Excavation
Look and feel

```html
<!DOCTYPE html>
<html lang="en">
<head>
<meta charset="utf-8">
<title>Tallow Ridge Pty Ltd – Business Card</title>
<link href="https://fonts.googleapis.com/css2?family=Rubik+Distressed&display=swap" rel="stylesheet">
<style>
  :root {
    --page: #ffffff;
    --front-bg: #000000;
    --back-bg: #111517;
    --swirl-grey: #3d3c3d;
    --ink: #ffffff;
    --ribbon-pink: #f29bc4;
    --ribbon-magenta: #e21f84;
    --ribbon-red: #e4312b;
    --ribbon-blue: #1b9ad6;
    --ribbon-sky: #7fcdf2;
    --ribbon-lime: #b7d97a;
    --ribbon-salmon: #f0806a;
  }
  html, body {
    margin: 0;
    padding: 0;
    overflow: hidden;
    background: var(--page);
  }
  .sheet {
    position: relative;
    width: 1200px;
    height: 441px;
    background: var(--page);
    overflow: hidden;
  }
  .card {
    position: absolute;
    top: 0;
    height: 441px;
    overflow: hidden;
  }
  .card--front {
    left: 0;
    width: 578px;
    background: var(--front-bg);
  }
  .card--back {
    left: 617px;
    width: 583px;
    background: var(--back-bg);
  }
  .front-swirls {
    position: absolute;
    left: 0;
    bottom: 0;
    width: 578px;
    height: 350px;
    background:
      radial-gradient(ellipse 420px 300px at 20% 100%, var(--swirl-grey) 0%, rgba(61,60,61,0.75) 45%, rgba(61,60,61,0) 100%),
      radial-gradient(ellipse 380px 140px at 70% 100%, rgba(61,60,61,0.8) 0%, rgba(61,60,61,0) 100%);
  }
  .front-details {
    position: absolute;
    right: 95px;
    top: 102px;
    margin: 0;
    text-align: right;
    font-family: "Rubik Distressed", sans-serif;
    font-size: 22px;
    line-height: 33px;
    color: var(--ink);
  }
  .front-details .company,
  .front-details .director,
  .front-details .phone {
    display: block;
  }
  .back-ribbons {
    position: absolute;
    left: 0;
    top: 0;
    width: 583px;
    height: 250px;
    background: linear-gradient(90deg,
      var(--ribbon-pink) 0%,
      var(--ribbon-magenta) 18%,
      var(--ribbon-red) 30%,
      var(--ribbon-blue) 50%,
      var(--ribbon-sky) 72%,
      var(--ribbon-lime) 100%);
    border-bottom-left-radius: 0 0;
    -webkit-mask-image: radial-gradient(ellipse 560px 250px at 62% 0%, #000 55%, rgba(0,0,0,0) 100%);
    mask-image: radial-gradient(ellipse 560px 250px at 62% 0%, #000 55%, rgba(0,0,0,0) 100%);
  }
  .services {
    position: absolute;
    left: 0;
    right: 0;
    top: 386px;
    margin: 0;
    text-align: center;
    font-family: "Rubik Distressed", sans-serif;
    font-size: 21px;
    letter-spacing: 0.5px;
    color: var(--ink);
  }
</style>
</head>
<body>
  <main class="sheet">
    <section class="card card--front">
      <div class="front-swirls" role="img" aria-label="Dense grey swirling line pattern rising from the bottom of the card"></div>
      <p class="front-details">
        <span class="company">Tallow Ridge Pty Ltd</span>
        <span class="director">Director Norman Cusk</span>
        <span class="phone">0462395108</span>
      </p>
    </section>
    <section class="card card--back">
      <div class="back-ribbons" role="img" aria-label="Sweeping arcs of colourful ribbons in pink, red, blue, sky blue and lime across the top of the card"></div>
      <p class="services">Landscape,Construction,Paving,Excavation</p>
    </section>
  </main>
</body>
</html>
```